Modern Banner and Window Decal Design For Law Firm Lawyer

We are looking for three modern and sophisticated banner design and window decal for our law firm.

Banner measurements/types:

1) Height: 130 cm Width: 160 cm (Outdoor banner)
2) Height: 200 cm Width: 85 cm (Pull up/retractable indoor banner)

Window Decal:
3) Height: 70cm width 70cm

Our law firm is based in Melbourne, Australia and we deal with property law mostly.

We prefer a white background with classic text in black or grey. We would also like a dash of colour so please use a green, blue or aqua colour palette that is consistent with our logo. Vector attached. A nice photo of property, Melbourne city viee, or family home would be nice.

We do not want any law related images - scales of justice, gavel or the like.

Our ultimate goal is to communicate that the firm is modern, professional and knowledgeable

We would like the following:

1. Our logo
2. Our services: - Property Law - Wills - Powers of Attorney - Probate - Estate Administration - Consultancy & Agency
3. Phone number
4. Web Address

5. For pull up/retractable banner we would also like the following text:

We use the latest digital technology and fixed-fees to provide fast and affordable legal advice that is easy to understand.

For privacy reasons, we will provide business details once we have decided on the winner.

We will monitor entries closely and promise to provide feedback and guidance on each entry.

Thank you very much for considering this project.

Target Market(s)

General public, professionals, lawyers and conveyancers

Industry/Entity Type

Law Firm

Font styles to use
Sans Serif

Colors
0393ce
34a6d7
0456a4
3176b5
acd037
33b8a4
86cfc6
00a990
9ccb3b

Requirements
Must have
• 1. Our logo
• 2. Our services: - Property Law - Wills - Powers of Attorney - Probate & Estate Administration - Consultancy & Agency
• 3. Phone number
• 4. Web Address
Nice to have
• Picture of Melbourne, Australia city ; property/buildings/lawyers
Should not have
• We do not want any law related images - scales of justice, gavel or the like.

```html
<!DOCTYPE html>
<html lang="en">
<head>
<meta charset="utf-8">
<title>Ridgeview Lawyers – Window Decal</title>
<link rel="stylesheet" href="https://fonts.googleapis.com/css2?family=Montserrat:wght@500;700&display=swap">
<style>
  :root {
    --page-bg: #e6e6e6;
    --decal-bg: #ffffff;
    --text-grey: #555759;
    --brand-aqua: #34a6d7;
    --brand-blue: #3176b5;
  }
  * { margin: 0; padding: 0; box-sizing: border-box; }
  html, body {
    width: 1200px;
    height: 1000px;
    overflow: hidden;
    background: var(--page-bg);
    font-family: "Montserrat", Arial, sans-serif;
  }
  .decal {
    position: absolute;
    left: 193px;
    top: 73px;
    width: 814px;
    height: 815px;
    background: var(--decal-bg);
  }
  .brand {
    position: absolute;
    left: 77px;
    top: 112px;
    display: flex;
    align-items: center;
    gap: 60px;
  }
  .brand-mark {
    width: 240px;
    height: 240px;
    border-radius: 50%;
    background: var(--brand-aqua);
  }
  .brand-name {
    color: var(--text-grey);
    font-weight: 500;
    font-size: 58px;
    line-height: 1.15;
    letter-spacing: 2px;
    text-transform: uppercase;
  }
  .services {
    position: absolute;
    left: 0;
    right: 0;
    top: 456px;
    text-align: center;
    color: var(--text-grey);
    font-weight: 700;
    font-size: 24px;
    line-height: 32px;
    letter-spacing: 0.3px;
    text-transform: uppercase;
  }
  .phone {
    position: absolute;
    left: 0;
    right: 0;
    top: 650px;
    display: flex;
    justify-content: center;
    align-items: center;
    gap: 18px;
    color: var(--text-grey);
    font-weight: 700;
    font-size: 66px;
    letter-spacing: 1px;
  }
  .phone-icon { width: 62px; height: 62px; flex: none; }
</style>
</head>
<body>
  <main class="decal">
    <div class="brand">
      <div class="brand-mark"></div>
      <div class="brand-name">Ridgeview<br>Lawyers</div>
    </div>

    <p class="services">
      Property Law | Wills | Powers of Attorney |<br>
      Probate | Estate Administration |<br>
      Consultancy &amp; Agency
    </p>

    <div class="phone">
      <svg class="phone-icon" viewBox="0 0 62 62" aria-hidden="true">
        <rect width="62" height="62" rx="10" fill="var(--brand-blue)"/>
        <path fill="#ffffff" d="M22 14c-2 0-6 3-6 7 0 12 13 27 26 27 4 0 7-4 7-6l-1-3-8-4-3 1-2 3c-5-2-9-6-11-11l3-2 1-3-4-8z"/>
      </svg>
      <span>555-0100-4821</span>
    </div>
  </main>
</body>
</html>
```